Business needs stationary

We are a company how capital venture and investment webcompany and work for international clients.

We need a stationary for a;

- email template
- business card
- web logo

Use the colors and elements plus company name in the attachment

Business card must include:

- company
- title
- adress
- phonenumber
- email adress
- website adress
- twitter
- facebook

We use the janeausten font. it's free. http://www.glyphorama.net/jane-austen.font

Investment

```html
<!DOCTYPE html>
<html lang="en">
<head>
<meta charset="utf-8">
<title>Harlan Reeve – Business Cards</title>
<link href="https://fonts.googleapis.com/css2?family=Open+Sans:wght@400;600&family=Pinyon+Script&display=swap" rel="stylesheet">
<style>
  :root{
    --page:#f4f5f7;
    --blue-deep:#0b3a66;
    --blue-mid:#125a9c;
    --blue-bright:#1f86d6;
    --charcoal:#1f2022;
    --charcoal-soft:#2b2d30;
    --accent-red:#e8483b;
    --text-light:#ffffff;
    --text-muted:#c9d3de;
    --rule-dash:#3d8fd6;
  }
  *{margin:0;padding:0;box-sizing:border-box}
  html,body{width:1200px;height:741px;overflow:hidden;background:var(--page)}
  .canvas{position:relative;width:1200px;height:741px;font-family:"Open Sans",sans-serif;color:var(--text-light)}
  .card{position:absolute;width:540px;height:320px;border-radius:3px;box-shadow:0 10px 28px rgba(0,0,0,.28);overflow:hidden}
  .blue-surface{background:linear-gradient(135deg,var(--blue-deep) 0%,var(--blue-mid) 30%,var(--blue-bright) 52%,var(--blue-mid) 70%,var(--blue-deep) 100%)}

  /* back card: split panels */
  .card-back{left:50px;top:70px;display:flex}
  .panel-brand{width:270px;height:100%;position:relative;border-right:2px dashed var(--rule-dash)}
  .panel-contact{width:270px;height:100%;background:linear-gradient(160deg,var(--charcoal) 0%,var(--charcoal-soft) 100%);padding:30px 26px 0 26px}

  .brand-block{display:flex;flex-direction:column;align-items:center;text-align:center}
  .brand-mark{width:26px;height:26px;background:var(--accent-red);margin-bottom:10px}
  .brand-name{font-weight:600;font-size:22px;letter-spacing:.5px;line-height:1.1}
  .brand-tagline{font-weight:600;font-size:11.5px;line-height:1.3;text-transform:uppercase;letter-spacing:.3px;margin-top:6px}

  .panel-brand .brand-block{position:absolute;left:0;right:0;top:88px}
  .social{position:absolute;left:0;right:0;top:238px;text-align:center;font-size:11.5px;line-height:1.45;color:var(--text-muted)}

  .person-name{font-family:"Pinyon Script",cursive;font-size:32px;line-height:1;color:var(--text-light)}
  .person-title{font-size:15px;letter-spacing:.8px;text-transform:uppercase;margin-top:4px;padding-bottom:12px;border-bottom:1px solid var(--accent-red)}
  .contact-row{padding:10px 0;border-bottom:1px solid var(--accent-red);font-size:11.5px;line-height:1.35;color:var(--text-muted)}
  .contact-row:last-child{border-bottom:none}
  .contact-icon{display:block;width:18px;height:14px;margin-bottom:3px}

  /* front card */
  .card-front{left:610px;top:350px}
  .card-front .brand-block{position:absolute;left:0;right:0;top:84px}
  .card-front .brand-mark{width:30px;height:30px}
  .card-front .brand-name{font-size:26px}
  .card-front .brand-tagline{font-size:13px}
  .web-address{font-size:14px;letter-spacing:.3px;margin-top:6px}
</style>
</head>
<body>
<main class="canvas">

  <section class="card card-back" aria-label="Business card, back">
    <div class="panel-brand blue-surface">
      <div class="brand-block">
        <span class="brand-mark"></span>
        <span class="brand-name">Harlan Reeve</span>
        <p class="brand-tagline">Growth Capital &amp;<br>Digital Equity Partners</p>
      </div>
      <p class="social">follow us: @harlanreeve<br>like our page: /harlanreeve</p>
    </div>

    <div class="panel-contact">
      <p class="person-name">Owen Castell</p>
      <p class="person-title">Account Manager</p>

      <div class="contact-row">
        <svg class="contact-icon" viewBox="0 0 18 14" aria-hidden="true"><rect x="1" y="1" width="16" height="12" rx="1" fill="var(--blue-mid)"/><path d="M1 2 L9 8 L17 2" stroke="var(--charcoal)" stroke-width="1.4" fill="none"/></svg>
        2240 Alder Crossing,<br>Suite C Maple Ridge, Oregon
      </div>
      <div class="contact-row">
        <svg class="contact-icon" viewBox="0 0 18 14" aria-hidden="true"><path d="M3 1 L6 1 L7 4 L5.5 5.5 C6.5 7.5 8 9 10 10 L11.5 8.5 L14.5 9.5 L14.5 12.5 C8 13 2.5 7.5 3 1 Z" fill="var(--blue-mid)"/></svg>
        T: 555-0148-2207<br>F: 555-0148-2209
      </div>
      <div class="contact-row">
        <svg class="contact-icon" viewBox="0 0 18 14" aria-hidden="true"><rect x="3" y="1" width="12" height="9" rx="1" fill="var(--blue-mid)"/><rect x="1" y="11" width="16" height="2" rx="1" fill="var(--blue-mid)"/></svg>
        info@harlanreeve.com<br>www.harlanreeve.com
      </div>
    </div>
  </section>

  <section class="card card-front blue-surface" aria-label="Business card, front">
    <div class="brand-block">
      <span class="brand-mark"></span>
      <span class="brand-name">Harlan Reeve</span>
      <p class="brand-tagline">Growth Capital &amp;<br>Digital Equity Partners</p>
      <p class="web-address">www.harlanreeve.com</p>
    </div>
  </section>

</main>
</body>
</html>
```